New Business Card Design Project

I need a meaningful new business card. Therefore, the website should convey growth, joy, uniqueness, workout and a bit of luxury.
Color scheme should be petrol, gold and matching colors.

```html
<!DOCTYPE html>
<html lang="de">
<head>
<meta charset="utf-8">
<title>Alpenkern Studio – Visitenkarte</title>
<link href="https://fonts.googleapis.com/css2?family=Lato:wght@400;700&family=Satisfy&display=block" rel="stylesheet">
<style>
  :root {
    --page-bg: #e6e4df;
    --petrol-deep: #0c2a30;
    --petrol: #14434b;
    --petrol-light: #1f5a63;
    --gold: #d4a233;
    --gold-line: #9a7630;
    --silver: #e4e8e8;
    --text-light: #f1f3f2;
  }
  * { box-sizing: border-box; margin: 0; padding: 0; }
  html, body {
    width: 1200px; height: 900px; overflow: hidden;
    background: var(--page-bg);
    font-family: "Lato", sans-serif;
  }
  .sheet {
    position: relative; width: 1200px; height: 900px;
    display: flex; flex-direction: column; align-items: center; justify-content: center; gap: 60px;
  }
  .card {
    position: relative; width: 580px; height: 360px;
    border-radius: 34px; overflow: hidden;
    box-shadow: 0 10px 28px rgba(0,0,0,0.25);
  }
  .card--front {
    background: radial-gradient(ellipse at 50% 40%, var(--petrol-light) 0%, var(--petrol-deep) 72%);
    display: flex; align-items: center; justify-content: center;
  }
  .card--back {
    background: linear-gradient(160deg, var(--petrol) 0%, var(--petrol-deep) 70%);
  }

  .brand { display: flex; align-items: center; gap: 14px; }
  .brand__dot { width: 22px; height: 22px; border-radius: 50%; }
  .brand__name { font-weight: 700; letter-spacing: 0.04em; }
  .brand--silver .brand__dot { background: var(--silver); }
  .brand--silver .brand__name { color: var(--silver); font-size: 38px; }

  .brand--gold { position: absolute; top: 44px; right: 40px; }
  .brand--gold .brand__dot { background: var(--gold); width: 18px; height: 18px; }
  .brand--gold .brand__name { color: var(--gold); font-size: 28px; }

  .contact { position: absolute; left: 44px; bottom: 24px; width: 400px; color: var(--text-light); }
  .contact__name {
    font-family: "Satisfy", "Brush Script MT", cursive;
    color: var(--gold); font-size: 38px; line-height: 1.1;
  }
  .contact__role { font-size: 17px; margin: 0 0 12px; }
  .contact__list { list-style: none; }
  .contact__item { display: flex; align-items: center; gap: 12px; font-size: 17px; line-height: 1.55; }
  .contact__icon { width: 16px; height: 16px; flex: none; fill: var(--gold); }
  .contact__icon--plain { width: 14px; height: 14px; border-radius: 50%; background: var(--gold); margin: 0 1px; }
  .contact__rule { height: 1px; background: var(--gold-line); margin: 12px 0 8px; }
  .contact__address { font-size: 16px; }
</style>
</head>
<body>
<main class="sheet">
  <section class="card card--front" aria-label="Vorderseite">
    <div class="brand brand--silver">
      <span class="brand__dot"></span>
      <span class="brand__name">Alpenkern Studio</span>
    </div>
  </section>

  <section class="card card--back" aria-label="Rückseite">
    <div class="brand brand--gold">
      <span class="brand__dot"></span>
      <span class="brand__name">Alpenkern Studio</span>
    </div>

    <div class="contact">
      <p class="contact__name">Clara Weidner</p>
      <p class="contact__role">Pilates Trainer</p>
      <ul class="contact__list">
        <li class="contact__item">
          <svg class="contact__icon" viewBox="0 0 24 24" aria-hidden="true"><path d="M6.6 10.8a15 15 0 0 0 6.6 6.6l2.2-2.2a1 1 0 0 1 1-.25 11.4 11.4 0 0 0 3.6.6 1 1 0 0 1 1 1V20a1 1 0 0 1-1 1A17 17 0 0 1 3 4a1 1 0 0 1 1-1h3.5a1 1 0 0 1 1 1c0 1.25.2 2.45.6 3.6a1 1 0 0 1-.25 1z"/></svg>
          +49 170 5550182
        </li>
        <li class="contact__item">
          <svg class="contact__icon" viewBox="0 0 24 24" aria-hidden="true"><path d="M2 5h20v14H2z M2 5l10 8 10-8" fill="none" stroke="#d4a233" stroke-width="2"/></svg>
          info@studio-alpenkern.de
        </li>
        <li class="contact__item">
          <svg class="contact__icon" viewBox="0 0 24 24" aria-hidden="true"><g fill="none" stroke="#d4a233" stroke-width="1.8"><circle cx="12" cy="12" r="9.5"/><ellipse cx="12" cy="12" rx="4.2" ry="9.5"/><path d="M2.5 12h19M4 7h16M4 17h16"/></g></svg>
          studio-alpenkern.de
        </li>
        <li class="contact__item">
          <span class="contact__icon contact__icon--plain" aria-hidden="true"></span>
          alpenkern_studio
        </li>
      </ul>
      <div class="contact__rule"></div>
      <p class="contact__address">Lindenweg 12, 83607 Holzkirchen</p>
    </div>
  </section>
</main>
</body>
</html>
```